Modern solo law firm website

I am preparing to launch a solo law practice (I own the domain harwenlegal.com and/or may use Harwen Law Office as a dba), and will need to move quickly to put up a website once I pull the trigger. There are many existing law firm sites to "copy," but I'm looking for something a little more modern and unique with some scrolling and modern icons (see e.g., trevinlaw.com). Right now, need the logo and skeleton for the site, as I have not written all of the content. For now, I like the idea of a simple home page that incorporates the phrase "Impactful. Valuable. Trusted." (Again, I may change that text.) And would like links on the home page across the top for "about", "services", "people" and "contact" -- these should lead to separate landing pages. The bottom of the home page also should have a link for a "disclaimer" and to Facebook, Twitter and LinkedIn (which I have not yet created). Make sense? Let me know if you have questions.

Target Market(s)

Business clients

Industry/Entity Type

Law Firm

Number of Pages Required

5+ page

Font styles to use
Other font styles liked:
• Perhaps Segoe UI

Requirements
Must have
• DRAFT STRUCTURE AND TEXT NOW ATTACHED. HOWEVER, SUBJECT TO EDITS BEING MADE CONCURRENTLY.

```html
<!DOCTYPE html>
<html lang="en">
<head>
<meta charset="utf-8">
<title>Harwen Legal</title>
<link rel="stylesheet" href="https://fonts.googleapis.com/css2?family=Open+Sans:wght@400;600;700&display=swap">
<style>
:root{
  --navy:#1d4a74;
  --title:#1f4f7d;
  --ink:#333a40;
  --muted:#555c63;
  --hero-dark:#1a1512;
  --btn-blue:#2b6a98;
  --btn-brown:#5b3a27;
  --about-a:#1c3f6e;
  --about-b:#1fc3a6;
  --contact:#22507a;
  --footer:#193a5a;
  --icon-dark:#3b3f44;
  --white:#ffffff;
}
*{box-sizing:border-box;margin:0;padding:0}
html,body{width:1200px;height:4196px;overflow:hidden}
body{font-family:"Open Sans",Arial,sans-serif;color:var(--ink);background:var(--white);position:relative}
section,header,footer{position:relative;width:1200px;overflow:hidden}
.abs{position:absolute}

/* hero */
.hero{height:727px;background:var(--hero-dark)}
.hero-photo{position:absolute;inset:0;background:
  radial-gradient(ellipse 420px 520px at 1000px 330px,#8a7a6c 0%,rgba(80,66,55,.6) 45%,rgba(0,0,0,0) 75%),
  linear-gradient(180deg,#141210 0%,#2a211b 52%,#6b4a30 72%,#3d2a1c 100%)}
.brand{left:100px;top:26px;font-size:32px;font-weight:600;color:var(--white);letter-spacing:.5px}
.nav{left:588px;top:30px;display:flex;gap:6px}
.nav a{color:var(--white);text-decoration:none;font-size:17px;padding:3px 12px}
.nav a.active{background:var(--btn-blue)}
.social{display:flex;gap:14px}
.social span{width:28px;height:28px;border-radius:50%;background:#d9d9d9;display:block}
.hero .social{left:980px;top:30px}
.hero-rule{left:100px;top:90px;width:996px;height:1px;background:rgba(255,255,255,.35)}
.arrow{top:340px;width:36px;height:36px;border:2px solid rgba(255,255,255,.5);border-radius:50%}
.hero-title{left:100px;top:432px;color:var(--white);font-size:25px;font-weight:700}
.hero-sub{left:100px;top:470px;color:var(--white);font-size:27px}
.btn{display:inline-block;color:var(--white);font-size:27px;text-align:center;line-height:52px;height:52px}
.btn-contact{left:100px;top:530px;width:219px;background:var(--btn-blue)}
.btn-more{left:339px;top:530px;width:218px;background:var(--btn-brown)}
.dots{left:575px;top:700px;display:flex;gap:8px}
.dots span{width:9px;height:9px;border-radius:50%;background:rgba(255,255,255,.5)}
.dots span.on{background:var(--white)}

/* intro */
.intro{height:666px;text-align:center}
.intro h2{padding-top:60px;font-size:38px;font-weight:700;color:var(--title);letter-spacing:.5px}
.intro .lede{font-size:27px;color:var(--title);margin-top:-4px}
.intro-text{width:1010px;margin:30px auto 0;text-align:left;font-size:14px;line-height:20px;color:var(--ink)}
.feature{position:absolute;width:470px;text-align:left}
.feature .badge{position:absolute;left:0;top:0;width:92px;height:92px;border-radius:50%;background:var(--icon-dark)}
.feature .badge.blue{background:var(--navy)}
.feature .badge svg{position:absolute;left:26px;top:26px}
.feature h3{margin-left:124px;font-size:23px;font-weight:400;color:var(--title);line-height:30px}
.feature p{margin-left:124px;font-size:12.5px;line-height:17px;color:var(--ink);width:330px}

/* about */
.about{height:607px;background:linear-gradient(160deg,var(--about-a) 0%,#1f5a86 45%,#1d7d99 70%,var(--about-b) 100%);color:var(--white)}
.about h2{position:absolute;top:48px;width:100%;text-align:center;font-size:38px;font-weight:700}
.about-photo{left:176px;top:151px;width:258px;height:380px;background:linear-gradient(180deg,#2a1d10 0%,#8a5a22 45%,#c99440 60%,#3a2410 100%)}
.about-text{left:331px;left:531px;top:149px;width:644px;font-size:13.4px;line-height:19.5px}

/* services */
.services{height:741px;background:linear-gradient(90deg,#e9eaeb 0%,#d2d5d7 40%,#e1e2e3 100%)}
.services h2{position:absolute;top:42px;width:100%;text-align:center;font-size:38px;font-weight:700;color:var(--title)}
.services .lede{position:absolute;top:105px;left:200px;width:800px;text-align:center;font-size:18px;line-height:24px;color:var(--ink)}
.svc{position:absolute;width:470px}
.svc svg{position:absolute;left:0;top:-6px}
.svc h3{margin-left:75px;font-size:15px;font-weight:700;color:var(--navy)}
.svc ul{margin:10px 0 0 120px;font-family:Arial,sans-serif;font-size:12.5px;line-height:17px;color:var(--muted);list-style:circle;width:340px}

/* people */
.people{height:817px;text-align:center}
.people h2{padding-top:45px;font-size:38px;font-weight:700;color:var(--title)}
.people-bio{width:1000px;margin:8px auto 0;font-size:13.5px;line-height:19.5px;color:var(--ink)}
.team{position:absolute;left:103px;top:358px;display:flex;gap:22px}
.member{width:232px;text-align:center}
.member .portrait{width:232px;height:300px;background:linear-gradient(180deg,#c9ced3 0%,#7b8896 55%,#2f3a48 100%)}
.member .name{margin-top:104px;font-family:Arial,sans-serif;font-size:19px;color:#222}
.member .role{font-family:Arial,sans-serif;font-size:11.5px;color:var(--muted)}
.member:nth-child(1) .name{margin-top:104px}

/* contact */
.contact{height:554px;background:var(--contact);color:var(--white)}
.contact h2{position:absolute;top:28px;width:100%;text-align:center;font-size:38px;font-weight:700;letter-spacing:.5px}
.contact .lede{position:absolute;top:76px;width:100%;text-align:center;font-size:14px}
.contact-rule{left:480px;top:114px;width:240px;height:2px;background:var(--white)}
.contact-rule::before,.contact-rule::after{content:"";position:absolute;top:-5px;width:12px;height:12px;border-radius:50%;background:var(--white)}
.contact-rule::before{left:-6px}.contact-rule::after{right:-6px}
.office{left:100px;top:173px}
.office h3{font-size:25px;font-weight:700;margin-bottom:20px}
.office li{list-style:none;font-size:15px;line-height:41px;display:flex;align-items:center;gap:12px}
.contact .social{margin-top:22px}
.contact .social span{background:var(--white)}
.field{background:var(--white);color:#9aa0a6;font-size:14px;padding:0 16px;position:absolute}
.f-name{left:613px;top:181px;width:235px;height:54px;line-height:54px}
.f-mail{left:866px;top:181px;width:234px;height:54px;line-height:54px}
.f-msg{left:613px;top:251px;width:487px;height:146px;padding-top:14px}
.send{left:613px;top:417px;width:134px;height:50px;line-height:50px;text-align:center;background:var(--btn-brown);color:var(--white);font-size:16px}
.to-top{left:1118px;top:470px;width:50px;height:50px;background:#c8cdd2}
.to-top svg{position:absolute;left:13px;top:13px}

/* footer */
.site-footer{height:84px;background:var(--footer);color:#c9d3de;text-align:center;font-size:12px;line-height:84px}
</style>
</head>
<body>

<header class="hero">
  <div class="hero-photo" role="img" aria-label="Photograph of a quill pen in an ink bottle on a wooden desk against a dark background"></div>
  <div class="abs brand">HARWEN LEGAL</div>
  <nav class="abs nav">
    <a class="active" href="#about">About</a><a href="#services">Services</a><a href="#people">People</a><a href="#contact">Contact</a>
  </nav>
  <div class="abs social" aria-label="Social links"><span></span><span></span><span></span></div>
  <div class="abs hero-rule"></div>
  <div class="abs arrow" style="left:18px"><svg width="32" height="32" viewBox="0 0 32 32"><path d="M18 10l-6 6 6 6" fill="none" stroke="#fff" stroke-width="2"/></svg></div>
  <div class="abs arrow" style="left:1146px"><svg width="32" height="32" viewBox="0 0 32 32"><path d="M14 10l6 6-6 6" fill="none" stroke="#fff" stroke-width="2"/></svg></div>
  <h1 class="abs hero-title">LOREM IPSUM DOLOR SIT</h1>
  <p class="abs hero-sub">Lorem ipsum Dolor Sit Contantry Popilar</p>
  <a class="abs btn btn-contact" href="#contact">Contact</a>
  <a class="abs btn btn-more" href="#about">Learn More</a>
  <div class="abs dots"><span></span><span class="on"></span><span></span></div>
</header>

<section class="intro">
  <h2>IMPACTFUL. VALUABLE. TRUSTED</h2>
  <p class="lede">How you should think of your lawyers, right?</p>
  <div class="intro-text">
    <p>Big Law plays an important part in the legal services industry. While you get the resources of a large organization, the services are costly and mis-incentivized so your lawyers benefit from taking longer and chasing every angle, regardless of whether it makes the most sense for your needs and budget. Been there, seen that.</p>
    <p>Harwen Legal is committed to making your life easier. To explore and listen to your true needs. To provide simple explanations that enable you to make the right business decisions. Harwen Legal is fully committed to providing high-impact work at an unquestionable value to help you achieve great success. And to earning your unwavering trust for the long haul.</p>
  </div>

  <div class="feature" style="left:100px;top:362px">
    <div class="badge blue"><svg width="40" height="40" viewBox="0 0 40 40"><circle cx="20" cy="11" r="7" fill="#fff"/><path d="M6 38c0-9 6-15 14-15s14 6 14 15z" fill="#fff"/></svg></div>
    <h3>Outside General Counsel</h3>
    <p>Maybe you have an in-house counsel, or maybe you don't. Harwen Legal can provide you with the in-house counsel services your company needs so your employees can focus on their primary jobs.</p>
  </div>
  <div class="feature" style="left:618px;top:362px">
    <div class="badge"><svg width="40" height="40" viewBox="0 0 40 40"><rect x="14" y="4" width="18" height="9" transform="rotate(40 23 8)" fill="#fff"/><rect x="10" y="18" width="4" height="16" transform="rotate(-50 12 26)" fill="#fff"/><rect x="4" y="33" width="20" height="4" fill="#fff"/></svg></div>
    <h3>Litigation and dispute resolution</h3>
    <p>Maybe you have an in-house counsel, or maybe you don't. Harwen Legal can provide you with the in-house counsel services your company needs so your employees can focus on their primary jobs.</p>
  </div>
  <div class="feature" style="left:100px;top:496px">
    <div class="badge"><svg width="40" height="40" viewBox="0 0 40 40"><circle cx="20" cy="12" r="6" fill="#fff"/><circle cx="8" cy="16" r="4.5" fill="#fff"/><circle cx="32" cy="16" r="4.5" fill="#fff"/><path d="M9 34c0-8 5-13 11-13s11 5 11 13z" fill="#fff"/><path d="M0 32c0-6 3-10 8-10 2 0 3 1 4 1-3 3-4 6-4 9z" fill="#fff"/><path d="M40 32c0-6-3-10-8-10-2 0-3 1-4 1 3 3 4 6 4 9z" fill="#fff"/></svg></div>
    <h3>Employment consulting</h3>
    <p>Maybe you have an in-house counsel, or maybe you don't. Harwen Legal can provide you with the in-house counsel services your company needs so your employees can focus on their primary jobs.</p>
  </div>
  <div class="feature" style="left:618px;top:496px">
    <div class="badge"><svg width="40" height="40" viewBox="0 0 40 40"><path d="M8 2h17l8 8v28H8z" fill="#fff"/><path d="M13 16h15M13 22h15M13 28h15" stroke="#3b3f44" stroke-width="2.5"/></svg></div>
    <h3>Business documents</h3>
    <p>Maybe you have an in-house counsel, or maybe you don't. Harwen Legal can provide you with the in-house counsel services your company needs so your employees can focus on their primary jobs.</p>
  </div>
</section>

<section class="about" id="about">
  <h2>ABOUT</h2>
  <div class="abs about-photo" role="img" aria-label="Photograph of brass scales of justice and a wooden gavel in warm light"></div>
  <div class="abs about-text">
    <p><strong>Harwen</strong> Legal was founded in 2014 by Scott Harwen, who has been helping clients solve their legal problems since 1998. Harwen Legal is dedicated to helping mature companies, small and medium-size businesses, and start-ups alike obtain superior results from their outside counsel at prices they find valuable. Impactful. Valuable. Trusted.</p>
    <p>How does one generate superior results at a great value? Scott Harwen believes it starts with being a good listener. His style is to work closely with clients to truly understand their legal problems and needs. He wants to get to know you really well, and understand what "success" means for your company. He will discuss the options in a way you can understand them, make actionable recommendations, and work with you to decide which path forward makes the most sense.</p>
    <p>Scott believes in devoting personal attention to every detail, providing direct personal contact as often as you need it, and being accessible and highly responsive. That means returning your calls and responding to your e-mails as soon as possible, answering any questions or concerns, and making sure you fully understand every recommended course of action – without legal jargon getting in the way. It also means keeping you posted regularly as work moves forward. Oh, and about that value. Harwen Legal values efficiency and cost certainty, just like its clients. The firm will work with you to find a solution that will fit your budget. And if the bill does not match the value you feel you received, Harwen Legal will work with you to make that right.</p>
    <p>Harwen Legal hopes its clients always arrive at a winning course of action that makes business sense. A lot of times, that advice may not be as profitable for the law firm but Harwen Legal wants you to come back with your next problem too.</p>
  </div>
</section>

<section class="services" id="services">
  <h2>SERVICES</h2>
  <p class="lede">Mr. Harwen has advised clients across a broad variety of industries and business and legal matters. Areas where Harwen Legal can help your company include:</p>

  <div class="svc" style="left:98px;top:190px">
    <svg width="40" height="40" viewBox="0 0 40 40"><circle cx="20" cy="10" r="7" fill="#2f5b86"/><path d="M6 40c0-11 6-17 14-17s14 6 14 17z" fill="#2f5b86"/><path d="M20 24l-3 6 3 10 3-10z" fill="#e4e6e8"/></svg>
    <h3>OUTSIDE GENERAL COUNSEL</h3>
    <ul><li>Regular interaction with your business and key decisionmakers</li><li>Strategic advisor for day-to-day legal affairs</li><li>Commercial contracts, licensing agreements andstrategic transactions</li><li>Document review</li><li>Human Resources matters</li><li>Proactive identification and preventive mitigation of legal exposures and risk</li><li>Managespecialized outside counsel, including their bills</li></ul>
  </div>
  <div class="svc" style="left:601px;top:190px">
    <svg width="40" height="40" viewBox="0 0 40 40"><rect x="14" y="4" width="18" height="9" transform="rotate(40 23 8)" fill="#3b2c22"/><rect x="10" y="18" width="4" height="16" transform="rotate(-50 12 26)" fill="#3b2c22"/><rect x="4" y="34" width="20" height="4" fill="#3b2c22"/></svg>
    <h3>LITIGATION AND DISPUTE RESOLUTION</h3>
    <ul><li>Regular interaction with your business and key decisionmakers</li><li>Strategic advisor for day-to-day legal affairs</li><li>Commercial contracts, licensing agreements andstrategic transactions</li><li>Document review</li><li>Human Resources matters</li><li>Proactive identification and preventive mitigation of legal exposures and risk</li><li>Managespecialized outside counsel, including their bills</li></ul>
  </div>
  <div class="svc" style="left:98px;top:452px">
    <svg width="44" height="40" viewBox="0 0 44 40"><circle cx="22" cy="12" r="6" fill="#5a2e22"/><circle cx="9" cy="15" r="4.5" fill="#5a2e22"/><circle cx="35" cy="15" r="4.5" fill="#5a2e22"/><path d="M11 32c0-8 5-13 11-13s11 5 11 13z" fill="#5a2e22"/><path d="M1 30c0-6 3-10 8-10l3 1c-3 3-4 6-4 9z" fill="#5a2e22"/><path d="M43 30c0-6-3-10-8-10l-3 1c3 3 4 6 4 9z" fill="#5a2e22"/></svg>
    <h3>EMPLOYMENT CONSULTING</h3>
    <ul><li>Regular interaction with your business and key decisionmakers</li><li>Strategic advisor for day-to-day legal affairs</li><li>Commercial contracts, licensing agreements andstrategic transactions</li><li>Document review</li><li>Human Resources matters</li><li>Proactive identification and preventive mitigation of legal exposures and risk</li><li>Managespecialized outside counsel, including their bills</li></ul>
  </div>
  <div class="svc" style="left:601px;top:452px">
    <svg width="40" height="40" viewBox="0 0 40 40"><path d="M9 2h16l7 7v29H9z" fill="none" stroke="#3b3f44" stroke-width="2.5"/><path d="M14 16h13M14 22h13M14 28h13" stroke="#3b3f44" stroke-width="2.5"/></svg>
    <h3>BUSINESS DOCUMENTS</h3>
    <ul><li>Regular interaction with your business and key decisionmakers</li><li>Strategic advisor for day-to-day legal affairs</li><li>Commercial contracts, licensing agreements andstrategic transactions</li><li>Document review</li><li>Human Resources matters</li><li>Proactive identification and preventive mitigation of legal exposures and risk</li><li>Managespecialized outside counsel, including their bills</li></ul>
  </div>
</section>

<section class="people" id="people">
  <h2>PEOPLE</h2>
  <div class="people-bio">
    <p>Scott Harwen is the owner of Harwen Legal. He spent 12 years at some of the best law firms in the country, working on high stakes, complex litigation for corporate clients. Four years ago, he founded the Lakeport office for the leading strategy and economic tech consulting firm serving high tech industry legal clients, and also serving as the firm's in-house counsel. Mr. Harwen is a lawyer, and breathes law. But these two other business exposures – economics and strategy – provided him with unique business acumen, project budgeting and management skills that law firms simply do not teach. Mr. Harwen is licensed to practice law in Illinois and is a member of the trial bar for the Northern District and many other federal appellate and trial courts throughout the country.</p>
    <p>Mr. Harwen received his law degree from the Lakeshore University School of Law in 1998, where he was a Edmund Hale Scholarship academic recipient and served as the Student Bar Association President. Before that, he received a B.A. with honors and with highest distinction from Midland University, where he was a Founders scholar.</p>
    <p>In addition to his law practice, Mr. Harwen is a member of the Zoning Board of Appeals for the City of Brookvale. He is also a long-time volunteer coach for his daughter's youth league soccer team and his son's Brookvale house-league baseball team.</p>
  </div>
  <div class="team">
    <div class="member"><div class="portrait" role="img" aria-label="Portrait photograph of Mark Ellis"></div><p class="name">Mark Ellis</p><p class="role">Founder &amp; CEO</p></div>
    <div class="member"><div class="portrait" role="img" aria-label="Portrait photograph of Nora Lane"></div><p class="name">Nora Lane</p><p class="role">Manager</p></div>
    <div class="member"><div class="portrait" role="img" aria-label="Portrait photograph of Paul Renner"></div><p class="name">Paul Renner</p><p class="role">Senior Lawyer</p></div>
    <div class="member"><div class="portrait" role="img" aria-label="Portrait photograph of Clara Voss"></div><p class="name">Clara Voss</p><p class="role">Lorem ipsum</p></div>
  </div>
</section>

<section class="contact" id="contact">
  <h2>CONTACT</h2>
  <p class="lede">Let's talk business, get in touch!</p>
  <div class="abs contact-rule"></div>
  <div class="abs office">
    <h3>Harwen Legal</h3>
    <ul>
      <li><svg width="14" height="18" viewBox="0 0 14 18"><path d="M7 0a7 7 0 0 1 7 7c0 5-7 11-7 11S0 12 0 7a7 7 0 0 1 7-7z" fill="#fff"/><circle cx="7" cy="7" r="2.5" fill="#22507a"/></svg>418 Alder St. Brookvale, IL 60299</li>
      <li><svg width="16" height="16" viewBox="0 0 16 16"><path d="M3 1l3 3-2 2c1 2 3 4 6 6l2-2 3 3-2 2C7 15 1 9 1 3z" fill="#fff"/></svg>555-014-2290</li>
      <li><svg width="16" height="12" viewBox="0 0 16 12"><rect width="16" height="12" fill="#fff"/><path d="M0 0l8 6 8-6" fill="none" stroke="#22507a" stroke-width="1.5"/></svg>info@harwenlegal.com</li>
    </ul>
    <div class="social" aria-label="Social links"><span></span><span></span><span></span></div>
  </div>
  <div class="field f-name">Name</div>
  <div class="field f-mail">Email (will not published)</div>
  <div class="field f-msg">Message</div>
  <div class="abs send">Send</div>
  <div class="abs to-top"><svg width="24" height="24" viewBox="0 0 24 24"><path d="M4 16l8-8 8 8" fill="none" stroke="#fff" stroke-width="3"/></svg></div>
</section>

<footer class="site-footer">(c) copyright 2014 Lorem ipsum dolor. All rights reserved</footer>

</body>
</html>
```